KORVAL Flyer

We need a flyer for the research project called 'KORVAL'. We will distribute this flyer during conferences and events to our audience (mainly industry (Security and IoT), medical organisations, and researchers) in order to provide the basic information about the project.
The project will provide a Holvane Shield Platform Toolkit for the Health-Care Industry.
We are attaching files to provide with concrete information on our requirements:
- KORVAL brochure content_final.ppt: includes the content we would like to include in the flyer. There is also the URL to the project website
- KORVAL layout.doc: it includes information about the layout (example video from another project brochure)
- KORVAL logo final version_sourcefile.zip: the project logo
- Logo-partners.zip: Logos that will be included (please follow the numbered order.)
We would like to use colors that belong to the project logo color range. Regarding the images that you may include in the brochure we wouldn't like to propose any because we do not want to limitate your imagination. They could be relevant to medical devices, security, etc.

```html
<!DOCTYPE html>
<html lang="en">
<head>
<meta charset="utf-8">
<title>KORVAL Flyer</title>
<link href="https://fonts.googleapis.com/css2?family=Barlow:wght@300;400;500;600;700&display=swap" rel="stylesheet">
<style>
:root{
  --teal:#1d9f8d;
  --teal-light:#35b8a3;
  --teal-dark:#148575;
  --grey:#8d8d8d;
  --grey-pale:#f2f3f3;
  --ink:#4f5656;
  --white:#ffffff;
  --eu:#2b4aa0;
}
*{box-sizing:border-box;margin:0;padding:0}
html,body{width:1200px;height:800px;overflow:hidden}
body{background:var(--white);font-family:"Barlow",sans-serif;color:var(--ink);position:relative}
.spread{position:absolute;left:125px;width:950px;height:328px;display:flex;box-shadow:0 1px 4px rgba(0,0,0,.12)}
.spread--outer{top:54px}
.spread--inner{top:418px}
.panel{position:relative;width:237.5px;height:100%;background:var(--grey-pale);overflow:hidden}
.panel--white{background:var(--white)}
.abs{position:absolute}
.hatch{background:var(--grey)}
.teal-block{background:linear-gradient(160deg,var(--teal-light),var(--teal) 55%,var(--teal-dark))}
.photo{position:absolute}
.photo--office{background:linear-gradient(135deg,#5c6468,#9aa3a6 45%,#c9cfd0 70%,#6f777a)}
.photo--theatre{background:linear-gradient(160deg,#eef3f6,#cfdde6 45%,#8fb0c8 70%,#e4ebef)}
.photo--lab{background:linear-gradient(120deg,#d8dcdd,#a9b0b2 40%,#e9ecec 70%,#7e8688)}
.logo{display:flex;align-items:center;gap:5px;color:var(--teal);font-weight:500;letter-spacing:1px}
.logo-dot{border:2px solid var(--teal);border-radius:50%}
.tiny{font-size:4px;line-height:5px}
.eu-bar{position:absolute;left:12px;display:flex;align-items:center;gap:4px;font-size:3px;line-height:3.6px;color:#777;width:200px}
.eu-flag{width:8px;height:5.5px;background:var(--eu);flex:none}
/* Get involved */
.involve-title{left:15px;top:26px;font-size:11.5px;font-weight:600;color:var(--teal)}
.involve-bar{left:9px;top:27px;width:2px;height:16px;background:var(--teal)}
.involve-sub{left:15px;top:40px;font-size:3.8px;color:#888}
.how-badge{left:88px;top:65px;background:var(--white);color:var(--teal);font-size:19px;font-weight:400;padding:0 4px;line-height:22px}
.visit{left:17px;top:100px;width:205px;color:var(--white);font-size:9.5px;line-height:11px}
.visit b{font-weight:600}
.check-list{left:18px;top:141px;list-style:none;color:var(--white);font-size:8px;font-weight:300}
.check-list li{display:flex;align-items:center;gap:6px;height:13.5px}
.check-list i,.where-list i{width:7px;height:7px;border-radius:50%;background:rgba(255,255,255,.45);border:1.5px solid rgba(255,255,255,.8);flex:none}
.rule{left:109px;top:234px;width:20px;height:1.5px;background:var(--white)}
.join{left:17px;top:262px}
.join-title{font-size:11px;color:var(--teal);font-weight:500}
.contact{display:flex;flex-direction:column;gap:1.5px;list-style:none;font-size:3.6px;color:#777}
.contact li{display:flex;align-items:center;gap:3px}
.contact li::before{content:"";width:3.5px;height:3.5px;border-radius:50%;background:var(--teal)}
.bottom-line{left:0;bottom:0;width:100%;height:3px;background:var(--teal)}
/* Cover */
.tagline{left:96px;top:235px;width:135px;font-size:10px;line-height:14px;color:var(--teal);font-weight:300}
.web{left:136px;top:301px;font-size:5.5px;letter-spacing:.8px;color:#666;border-bottom:1px solid var(--teal);padding-bottom:2px}
.frame-line{background:var(--teal)}
/* Inner: what is */
.tab{left:53px;top:2px;width:134px;height:22px;background:var(--teal);clip-path:polygon(6% 0,100% 0,94% 100%,0 100%);color:var(--white);font-size:13px;font-weight:600;text-align:center;line-height:22px}
.h-teal{color:var(--teal);font-weight:700;font-size:9.5px}
.body-s{font-size:5px;line-height:6px;color:var(--ink)}
.dot-list{list-style:none;font-size:5px;color:var(--ink)}
.dot-list li{display:flex;align-items:center;gap:3px;height:9.6px}
.dot-list li::before{content:"";width:4px;height:4px;border-radius:50%;border:1px solid var(--teal)}
/* Pilot */
.pilot-title{left:0;width:100%;top:2px;text-align:center;font-size:35px;font-weight:700;color:var(--teal)}
.pill{left:61px;top:54px;width:116px;height:14px;border-radius:7px;background:var(--white);color:var(--teal-dark);font-size:9px;font-weight:700;text-align:center;line-height:14px}
.pilot-text{left:20px;top:78px;width:198px;text-align:center;color:var(--white);font-size:5px;line-height:6px}
.where{left:19px;top:113px;color:var(--white);font-size:13px;font-weight:500}
.where-list{left:20px;top:135px;list-style:none;color:var(--white);font-size:8px;font-weight:300;width:210px}
.where-list li{display:flex;gap:5px;line-height:13.5px}
.where-list i{margin-top:3px}
.how2{left:19px;top:242px;font-size:13px;font-weight:600;color:var(--teal)}
.how2-text{left:20px;top:263px;width:200px}
/* Why */
.why-bar{left:0;top:3px;width:238px;height:24px;background:var(--teal);color:var(--white);font-size:12.5px;font-weight:600;line-height:24px;padding-left:19px}
.reason{position:absolute;left:20px;width:210px;display:flex;gap:6px}
.reason-icon{width:18px;height:18px;border-radius:50%;background:var(--teal);border:2px solid #cfe9e4;flex:none;display:flex;align-items:center;justify-content:center}
.reason-title{font-size:7.5px;font-weight:600;color:var(--teal);line-height:9px}
.reason-text{font-size:3.7px;line-height:4.5px;color:#666;margin-top:1px}
/* Partners */
.partners-pill{left:57px;top:62px;width:138px;height:18px;background:#9c9c9c;border-radius:3px;color:var(--white);font-size:11.5px;font-weight:600;text-align:center;line-height:18px}
.badge{position:absolute;background:#c3c7c7}
</style>
</head>
<body>

<!-- Outer spread -->
<section class="spread spread--outer">
  <div class="panel">
    <div class="abs hatch" style="left:0;top:0;width:53px;height:101px"></div>
    <div class="abs hatch" style="left:0;top:226px;width:53px;height:101px"></div>
    <div class="photo photo--office" role="img" aria-label="Team working together at desks in a modern office" style="left:2px;top:105px;width:167px;height:118px"></div>
    <div class="abs teal-block" style="left:174px;top:105px;width:64px;height:118px"></div>
  </div>

  <div class="panel panel--white">
    <div class="abs involve-bar"></div>
    <h2 class="abs involve-title">Get involved in our project activities!</h2>
    <p class="abs involve-sub">Take part in the KORVAL yearly workshops and organized events and activities.</p>
    <div class="abs teal-block" style="left:0;top:61px;width:100%;height:190px"></div>
    <div class="abs how-badge">How?</div>
    <p class="abs visit">Visit our website <b>https://korval-project.eu/</b><br>and join our community:</p>
    <ul class="abs check-list">
      <li><i></i>Join our social media channels</li>
      <li><i></i>Subscribe to our Newsletter</li>
      <li><i></i>Check our upcoming events to participate</li>
    </ul>
    <div class="abs rule"></div>
    <div class="abs join">
      <div class="logo-dot" style="width:12px;height:12px;margin-left:12px"></div>
      <div class="join-title">Join us</div>
    </div>
    <ul class="abs contact" style="left:17px;top:293px">
      <li>Video channel: The korval project</li>
      <li>Web: https://korval-project.eu/</li>
    </ul>
    <ul class="abs contact" style="left:129px;top:293px">
      <li>Microblog: @KorvalProject</li>
      <li>Community page: korval-project</li>
      <li>Professional page: korval-project</li>
    </ul>
    <div class="eu-bar" style="top:315px"><span class="eu-flag"></span><span>This project has received funding from a European research and innovation programme under grant agreement.</span></div>
    <div class="abs bottom-line"></div>
  </div>

  <div class="panel panel--white">
    <div class="abs" style="left:0;top:0;width:45px;height:61px;background:var(--grey-pale)"></div>
    <div class="abs logo" style="left:120px;top:30px;font-size:17px"><span class="logo-dot" style="width:18px;height:18px"></span>KORVAL</div>
    <div class="abs teal-block" style="left:0;top:61px;width:92px;height:248px"></div>
    <div class="photo photo--theatre" role="img" aria-label="Bright hospital operating theatre with medical equipment" style="left:12px;top:78px;width:204px;height:136px"></div>
    <div class="abs frame-line" style="left:223px;top:170px;width:1px;height:54px"></div>
    <div class="abs frame-line" style="left:180px;top:224px;width:44px;height:1px"></div>
    <p class="abs tagline">A Holvane Shield Platform Toolkit for the Health-Care Industry</p>
    <p class="abs web">www.korval-project.eu</p>
  </div>

  <div class="panel">
    <div class="abs teal-block" style="left:0;top:105px;width:63px;height:118px"></div>
    <div class="photo photo--lab" role="img" aria-label="Researchers working at computers in a laboratory" style="left:69px;top:105px;width:169px;height:118px"></div>
    <div class="abs hatch" style="left:185px;top:0;width:53px;height:101px"></div>
    <div class="abs hatch" style="left:185px;top:226px;width:53px;height:101px"></div>
  </div>
</section>

<!-- Inner spread -->
<section class="spread spread--inner">
  <div class="panel panel--white">
    <h2 class="abs tab">What is KORVAL?</h2>
    <h3 class="abs h-teal" style="left:20px;top:35px">The Challenge</h3>
    <p class="abs body-s" style="left:26px;top:47px;width:190px">Solving the Riddle of Cyber-Security protection in Healthcare IT ecosystems.</p>
    <h3 class="abs h-teal" style="left:20px;top:70px">How does KORVAL tackle the challenge?</h3>
    <p class="abs body-s" style="left:26px;top:83px">Through:</p>
    <ul class="abs dot-list" style="left:20px;top:91px">
      <li>Cyber protection and data privacy and integrity</li>
      <li>The proactive assessment and mitigation of Cyber-Security threats</li>
      <li>Evaluation and verification of new Medical Devices and Services</li>
      <li>Providing the KORVAL Certification</li>
      <li>Near real time vulnerability assessment of operating IT Ecosystems</li>
    </ul>
    <h3 class="abs h-teal" style="left:20px;top:147px">Pilot</h3>
    <p class="abs body-s" style="left:26px;top:160px;width:190px">The KORVAL proposed technology and business framework will be demonstrated and validated under realistic operating conditions and various use case scenarios.</p>
    <div class="abs teal-block" style="left:0;top:235px;width:100%;height:93px"></div>
    <div class="photo photo--office" role="img" aria-label="Colleagues discussing a project in an open office" style="left:34px;top:188px;width:169px;height:118px"></div>
  </div>

  <div class="panel panel--white">
    <h2 class="abs pilot-title">Pilot</h2>
    <div class="abs teal-block" style="left:0;top:44px;width:100%;height:191px"></div>
    <div class="abs pill">Did you know that</div>
    <p class="abs pilot-text">The project's pilots will deploy and evaluate the KORVAL solution at business as usual and emergency situations across various use cases at three different countries.</p>
    <h3 class="abs where">Where?</h3>
    <ul class="abs where-list">
      <li><i></i>Hospital Santa Lúcia de Almara in Portugal</li>
      <li><i></i>Hospital Vireo Medical in Romania</li>
      <li><i></i>The 3rd Health Regional Authority of Orvenia<br>and Kallis in Greece</li>
    </ul>
    <h3 class="abs how2">How?</h3>
    <p class="abs body-s how2-text">The overall solution will be evaluated using Key Performance Indicators related with the KORVAL cyber-security effectiveness, usability and cost-effectiveness, by end-users, project partners and business stakeholders.</p>
    <div class="eu-bar" style="top:316px"><span class="eu-flag"></span><span>This project has received funding from a European research and innovation programme.</span></div>
  </div>

  <div class="panel panel--white">
    <h2 class="abs why-bar">Why KORVAL is important for you?</h2>
    <div class="reason" style="top:40px"><span class="reason-icon"></span><div><div class="reason-title">Industry (Security and IoT)</div><p class="reason-text">KORVAL will provide tools to evaluate healthcare devices and services and receive a detailed compliance and certification report that assesses if the device or service is vulnerable, misused, or if its attack surface lacks crucial security requirements.</p></div></div>
    <div class="reason" style="top:78px"><span class="reason-icon"></span><div><div class="reason-title">Medical organisations</div><p class="reason-text">The KORVAL ecosystem will armour medical organisations from multiple cybersecurity threats and protect patient data. It will provide the means for medical organisations to become aware of their cyber-security risks and privacy policy, and to make informed decisions on KORVAL certified devices.</p></div></div>
    <div class="reason" style="top:116px"><span class="reason-icon"></span><div><div class="reason-title">Society</div><p class="reason-text">KORVAL will give patients the strong feeling that their data are secure. It will help patients increase their control over their multiple IoT devices, choosing those available in the market based on KORVAL certification.</p></div></div>
    <div class="reason" style="top:153px"><span class="reason-icon"></span><div><div class="reason-title">Research</div><p class="reason-text">Through the extensive research of this Research and Innovation project, KORVAL will produce research articles and technical demonstrations at journals and conferences, as well as a community of developers and scientists.</p></div></div>
    <div class="reason" style="top:189px"><span class="reason-icon"></span><div><div class="reason-title">Policy</div><p class="reason-text">KORVAL will investigate improvements and alternatives to current institutional and governance frameworks in order to improve cybersecurity awareness and stimulate usage of the proposed solution, aiming to empower patient data privacy.</p></div></div>
    <div class="reason" style="top:225px"><span class="reason-icon"></span><div><div class="reason-title">International networks</div><p class="reason-text">Through international networks, KORVAL will increase awareness to several stakeholders about the project's achievements. KORVAL will seek opportunities to participate in relevant activities organised by the international network, and share online information published by KORVAL through channels such as websites and social networks.</p></div></div>
    <div class="reason" style="top:266px"><span class="reason-icon"></span><div><div class="reason-title">Related EU-funded projects</div><p class="reason-text">By cooperating with KORVAL, other EU-funded projects can develop more impactful and sustainable cybersecurity environments in the health sector, and enhance their ability to Disseminate and Communicate their results.</p></div></div>
    <div class="eu-bar" style="top:316px"><span class="eu-flag"></span><span>This project has received funding from a European research and innovation programme.</span></div>
  </div>

  <div class="panel">
    <div class="abs logo" style="left:66px;top:14px;font-size:24px"><span class="logo-dot" style="width:28px;height:28px;border-width:3px"></span>KORVAL</div>
    <h2 class="abs partners-pill">KORVAL partners</h2>
    <div class="badge" style="left:21px;top:109px;width:19px;height:19px;border-radius:50%"></div>
    <div class="badge" style="left:58px;top:109px;width:40px;height:16px"></div>
    <div class="badge" style="left:112px;top:112px;width:58px;height:11px"></div>
    <div class="badge" style="left:178px;top:111px;width:44px;height:13px"></div>
    <div class="badge" style="left:20px;top:152px;width:48px;height:13px"></div>
    <div class="badge" style="left:76px;top:151px;width:40px;height:13px"></div>
    <div class="badge" style="left:122px;top:152px;width:50px;height:11px"></div>
    <div class="badge" style="left:178px;top:152px;width:44px;height:10px"></div>
    <div class="badge" style="left:20px;top:186px;width:20px;height:24px"></div>
    <div class="badge" style="left:48px;top:193px;width:46px;height:11px"></div>
    <div class="badge" style="left:113px;top:190px;width:52px;height:17px"></div>
    <div class="badge" style="left:170px;top:193px;width:52px;height:11px"></div>
    <div class="badge" style="left:19px;top:232px;width:56px;height:11px"></div>
    <div class="badge" style="left:100px;top:232px;width:50px;height:11px"></div>
    <div class="badge" style="left:168px;top:229px;width:48px;height:16px"></div>
    <div class="badge" style="left:60px;top:269px;width:74px;height:13px"></div>
    <div class="badge" style="left:146px;top:266px;width:42px;height:18px"></div>
    <div class="eu-bar" style="top:316px"><span class="eu-flag"></span><span>This project has received funding from a European research and innovation programme.</span></div>
  </div>
</section>

</body>
</html>
```